COMING SOON PAGE for BEAUTY WEBSITE

Looking for a very beautiful, high end coming soon page for the site, www.glowparlorqz.com

looking for the site to have a bit of text and fade thru a few images -- beautiful fonts, modern airy feel.

Text on page:

it doesn't have to be complicated
glowparlorqz.com coming soon
beauty, simplified.

Please use all lowercase and place the logo somewhere on the page...logo attached and images attached -- happy to provide more images if necessary

You can play with images, zoom in, dont need to use whole image, etc....modern, classy, airy.

thanks.

Target Market(s)

35-60 year old women, modern, elegant, look conscious

Number of Pages Required

1 page

Font styles to use
Sans Serif

Requirements
Must have
• Images fade from one to other slowly and elegantly -- or slide, etc..some sort of elegant transition
• Opaque, airy feel
• logo must be present and easy to identify
Should not have
• NO SOUND
• NO SCRIPT TEXT

```html
<!DOCTYPE html>
<html lang="en">
<head>
<meta charset="utf-8">
<title>glowparlorqz – coming soon</title>
<link rel="stylesheet" href="https://fonts.googleapis.com/css2?family=Quicksand:wght@300;400;500&family=Nunito+Sans:wght@300;400;600&display=swap">
<style>
  :root {
    --stage: #2b2b2b;
    --paper: #ffffff;
    --bar-top: #1c1c1c;
    --bar-bottom: #000000;
    --bar-edge: #3a3a3a;
    --ink: #111111;
    --muted: #8a8a8a;
    --teal: #5ccbcf;
    --teal-deep: #3fb8bd;
    --field: #f4f6f6;
  }
  * { box-sizing: border-box; margin: 0; padding: 0; }
  html, body { width: 1200px; height: 960px; overflow: hidden; }
  body { background: var(--stage); font-family: "Quicksand", sans-serif; }

  .page {
    position: absolute; left: 0; top: 142px;
    width: 1200px; height: 676px;
    background: var(--paper);
    overflow: hidden;
  }

  .topbar { position: absolute; left: 0; top: 0; width: 1200px; height: 42px; }
  .topbar svg { position: absolute; left: 0; top: 0; }

  .social { position: absolute; top: 12px; left: 988px; display: flex; gap: 10px; }
  .social span { width: 18px; height: 18px; background: var(--paper); border-radius: 2px; display: block; }

  .menu { position: absolute; left: 1149px; top: 16px; width: 26px; }
  .menu span { display: block; height: 3px; background: #222; margin-bottom: 4px; border-radius: 1px; }

  .hero-photo {
    position: absolute; left: 0; top: 42px; width: 748px; height: 634px;
    background:
      radial-gradient(ellipse 30% 28% at 48% 62%, #e8c6a8 0%, rgba(232,198,168,0) 100%),
      radial-gradient(ellipse 45% 50% at 38% 48%, rgba(146,92,56,0.55) 0%, rgba(146,92,56,0) 100%),
      linear-gradient(160deg, #f4f2ee 0%, #e9ddd0 45%, #8a7c72 78%, #cfcac4 100%);
  }

  .glow {
    position: absolute; left: 760px; top: 60px; width: 440px; height: 560px;
    background: radial-gradient(ellipse 55% 50% at 45% 55%, #f1f2f2 0%, rgba(255,255,255,0) 100%);
  }

  .intro { position: absolute; left: 826px; top: 252px; width: 300px; }
  .tagline { font-size: 17px; font-weight: 300; color: var(--muted); letter-spacing: 0.2px; }
  .brand { font-size: 30px; font-weight: 400; color: var(--ink); line-height: 1.1; margin-top: 2px; letter-spacing: -0.5px; }

  .coming {
    position: absolute; left: 751px; top: 328px; width: 403px;
    display: flex; align-items: center; justify-content: space-between;
  }
  .coming .rule { width: 65px; height: 9px; border-top: 2px solid var(--teal); border-bottom: 2px solid var(--teal); }
  .coming h1 { font-size: 43px; font-weight: 400; color: var(--teal); line-height: 1; letter-spacing: 0.5px; }

  .motto { position: absolute; left: 752px; top: 386px; width: 400px; text-align: center; font-size: 16px; font-weight: 300; color: var(--muted); }

  .notify { position: absolute; left: 766px; top: 528px; width: 373px; font-family: "Nunito Sans", sans-serif; }
  .notify p { text-align: center; font-size: 14px; font-weight: 300; color: var(--muted); margin-bottom: 8px; }
  .notify form { display: flex; height: 34px; border: 2px solid var(--teal-deep); border-radius: 6px; overflow: hidden; }
  .notify input {
    flex: 1; border: 0; background: linear-gradient(#fff, var(--field));
    font-family: "Nunito Sans", sans-serif; font-size: 14px; font-weight: 300; padding: 0 11px; color: var(--ink);
  }
  .notify input::placeholder { color: #9a9a9a; }
  .notify button {
    width: 87px; border: 0; background: linear-gradient(var(--teal), var(--teal-deep));
    color: #fff; font-family: "Nunito Sans", sans-serif; font-size: 14px; font-weight: 600;
  }
</style>
</head>
<body>
  <main class="page">
    <header class="topbar">
      <svg width="1200" height="42" viewBox="0 0 1200 42" aria-hidden="true">
        <defs>
          <linearGradient id="barFill" x1="0" y1="0" x2="0" y2="1">
            <stop offset="0" stop-color="#262626"/>
            <stop offset="1" stop-color="#000"/>
          </linearGradient>
        </defs>
        <polygon points="0,0 1135,0 1118,42 0,42" fill="url(#barFill)"/>
        <polygon points="0,37 1120,37 1118,42 0,42" fill="#3a3a3a"/>
      </svg>
      <nav class="social" aria-label="social links">
        <span></span><span></span><span></span><span></span>
      </nav>
      <div class="menu" aria-label="menu"><span></span><span></span><span></span></div>
    </header>

    <div class="hero-photo" role="img" aria-label="photo of a woman lying with long brown dreadlocks spread out, wearing a black and white checked shirt"></div>

    <div class="glow"></div>

    <div class="intro">
      <p class="tagline">it doesn't have to be complicated</p>
      <p class="brand">glowparlorqz</p>
    </div>

    <div class="coming">
      <span class="rule"></span>
      <h1>coming soon</h1>
      <span class="rule"></span>
    </div>

    <p class="motto">beauty, simplified.</p>

    <section class="notify">
      <p>Get notified when our web site is live online</p>
      <form>
        <input type="email" placeholder="Enter your e-mail here">
        <button type="button">Notify Me</button>
      </form>
    </section>
  </main>
</body>
</html>
```